Rocket business card

Modern business card design, use of color is good with clean space too.

Things to include on card:

Quote: I add fuel to your optometry practice

- Eyewear Sales
- Admin Duties
- Revenue Collection
- Leadership
- Tech Adoption
- COGS Reduction
- Product Sourcing
-Medical Growth

Dalton Vessey, CEO
Glint Harbor
Text Me! 847-302-1964
dalton@glintharbor.example

```html
<!DOCTYPE html>
<html lang="en">
<head>
<meta charset="utf-8">
<title>Glint Harbor – Business Card</title>
<link rel="stylesheet" href="https://fonts.googleapis.com/css2?family=Montserrat:wght@400;500&family=Roboto:wght@400&display=swap">
<style>
  :root {
    --stage: #2b2b2d;
    --card-dark: #0c0c0c;
    --card-light: #f7f7f7;
    --ink: #111111;
    --paper: #ffffff;
    --accent: #e8422a;
    --accent-warm: #f28a22;
    --watermark: #e7e7e7;
  }
  * { box-sizing: border-box; margin: 0; padding: 0; }
  html, body {
    width: 1200px; height: 880px; overflow: hidden;
    background: var(--stage);
    font-family: "Montserrat", sans-serif;
  }
  .stage { position: relative; width: 1200px; height: 880px; }
  .card {
    position: absolute; width: 580px; height: 332px;
    border-radius: 18px; overflow: hidden;
    box-shadow: 0 14px 32px rgba(0,0,0,.45);
  }
  .brand-dot {
    width: 44px; height: 44px; border-radius: 50%; flex: none;
    background: linear-gradient(160deg, var(--accent-warm), var(--accent));
  }
  .brand-name {
    font-weight: 400; letter-spacing: 1px;
    text-transform: uppercase; white-space: nowrap;
  }

  /* Back: services */
  .card-back { left: 110px; top: 70px; background: var(--card-dark); color: var(--paper); }
  .card-back .brand {
    position: absolute; left: 44px; top: 110px; width: 260px;
    display: flex; flex-direction: column; align-items: center; gap: 14px;
  }
  .card-back .brand-dot { width: 62px; height: 62px; }
  .card-back .brand-name { color: var(--paper); font-size: 28px; }
  .services {
    position: absolute; left: 350px; top: 46px; list-style: none;
  }
  .services li {
    display: flex; align-items: center; gap: 12px;
    font-family: "Roboto", sans-serif; font-size: 15px;
    height: 30px; white-space: nowrap;
  }
  .services li::before {
    content: ""; width: 11px; height: 11px; border-radius: 50%;
    border: 2px solid var(--paper); flex: none;
  }

  /* Front: contact */
  .card-front { left: 510px; top: 470px; background: var(--card-light); color: var(--ink); }
  .watermark-circle {
    position: absolute; left: -40px; top: 20px;
    width: 250px; height: 250px; border-radius: 50%;
    border: 26px solid var(--watermark);
  }
  .card-front .brand {
    position: absolute; right: 40px; top: 46px;
    display: flex; align-items: center; gap: 14px;
  }
  .card-front .brand-name { color: var(--ink); font-size: 32px; }
  .rule-top {
    position: absolute; right: 36px; top: 128px;
    width: 300px; height: 1px; background: var(--ink);
  }
  .contact {
    position: absolute; right: 36px; top: 146px;
    list-style: none; font-family: "Roboto", sans-serif; font-size: 14px;
  }
  .contact li { display: flex; align-items: center; gap: 8px; height: 26px; white-space: nowrap; }
  .contact .icon {
    width: 18px; height: 18px; border-radius: 50%;
    background: linear-gradient(160deg, var(--accent-warm), var(--accent));
    display: flex; align-items: center; justify-content: center; flex: none;
  }
  .contact .label { color: var(--accent); }
  .rule-bottom {
    position: absolute; left: 36px; bottom: 72px;
    width: 320px; height: 1px; background: var(--ink);
  }
  .signature {
    position: absolute; left: 40px; bottom: 36px;
    font-size: 20px; font-weight: 400; text-transform: uppercase; letter-spacing: .5px;
    white-space: nowrap;
  }
  .signature .title { color: var(--accent); }
</style>
</head>
<body>
<main class="stage">

  <section class="card card-back" aria-label="Card back: services">
    <div class="brand">
      <span class="brand-dot"></span>
      <span class="brand-name">Glint Harbor</span>
    </div>
    <ul class="services">
      <li>Eyewear Sales</li>
      <li>Admin Duties</li>
      <li>Revenue Collection</li>
      <li>Leadership</li>
      <li>Tech Adoption</li>
      <li>COGS Reduction</li>
      <li>Product Sourcing</li>
      <li>Medical Growth</li>
    </ul>
  </section>

  <section class="card card-front" aria-label="Card front: contact">
    <div class="watermark-circle"></div>
    <div class="brand">
      <span class="brand-dot"></span>
      <span class="brand-name">Glint Harbor</span>
    </div>
    <div class="rule-top"></div>
    <ul class="contact">
      <li>
        <span class="icon">
          <svg width="10" height="10" viewBox="0 0 10 10"><path d="M1 2h8v5H4L2 9V7H1z" fill="#fff"/></svg>
        </span>
        <span><span class="label">Text Me!</span> 847-302-1964</span>
      </li>
      <li>
        <span class="icon">
          <svg width="10" height="10" viewBox="0 0 10 10"><rect x="1" y="2.5" width="8" height="5" fill="none" stroke="#fff" stroke-width="1"/><path d="M1 2.5l4 3 4-3" fill="none" stroke="#fff" stroke-width="1"/></svg>
        </span>
        <span>dalton@glintharbor.example</span>
      </li>
    </ul>
    <div class="rule-bottom"></div>
    <p class="signature">Dalton Vessey, <span class="title">CEO</span></p>
  </section>

</main>
</body>
</html>
```